Valto Sàrl - Business Card

VALTO Sàrl operates in the sector Services for banks and credit institutions. It is a B2B which connects companies. The main colors should be Blue and Black. The logo and look of the card should be simple, professional, conservative and reflect Connecting People.

Target Market(s)

Financial professionals and institutions

Industry/Entity Type

Finance

Contact Information for Business Card

Chemin des Prés 9
1027 Lonay

Logo Text

Valto Sàrl

Font styles to use
Serif
Sans Serif

Colors
0355a3
3176b5
85acd3
cfdeed

Requirements
Should not have
• Multiple colors

```html
<!DOCTYPE html>
<html lang="fr">
<head>
<meta charset="utf-8">
<title>Valto Sàrl – Business Card</title>
<link href="https://fonts.googleapis.com/css2?family=Montserrat:wght@400;500;600&display=swap" rel="stylesheet">
<style>
  :root{
    --blue:#0355a3;
    --blue-mid:#3176b5;
    --blue-light:#85acd3;
    --blue-pale:#cfdeed;
    --black:#1b1c1e;
    --ink:#3a3b3d;
    --paper:#ffffff;
    --backdrop:#e6e7ea;
  }
  *{margin:0;padding:0;box-sizing:border-box}
  html,body{width:1200px;height:716px;overflow:hidden}
  body{
    background:var(--backdrop);
    font-family:"Montserrat",sans-serif;
    position:relative;
  }
  .card{
    position:absolute;
    top:210px;
    width:520px;
    height:297px;
    border-radius:4px;
    overflow:hidden;
    box-shadow:0 6px 18px rgba(0,0,0,.18);
  }
  /* Front */
  .card-front{
    left:50px;
    background:var(--black);
    border-bottom:5px solid var(--blue-mid);
    display:flex;
    align-items:center;
    justify-content:center;
  }
  .brand{
    display:flex;
    align-items:center;
    gap:12px;
  }
  .brand-dot{
    width:22px;height:22px;border-radius:50%;
    background:var(--blue-mid);
  }
  .brand-name{
    font-weight:600;
    font-size:28px;
    letter-spacing:2px;
    color:var(--blue-mid);
    text-transform:uppercase;
  }
  /* Back */
  .card-back{
    left:630px;
    background:var(--paper);
  }
  .wave{position:absolute;left:0;top:0;width:520px;height:297px}
  .identity{
    position:absolute;left:38px;top:58px;
  }
  .person-name{
    font-weight:500;
    font-size:19px;
    letter-spacing:.5px;
    color:var(--blue);
    text-transform:uppercase;
  }
  .person-role{
    font-size:11px;
    color:var(--ink);
    margin-top:1px;
  }
  .rule{
    position:absolute;left:38px;top:104px;
    width:444px;height:1px;background:var(--blue-mid);
  }
  .contacts{
    position:absolute;left:38px;top:118px;
    list-style:none;
    font-size:11px;
    color:var(--ink);
    line-height:18px;
  }
  .contacts li{display:flex;align-items:center;gap:7px}
  .contacts svg{width:9px;height:9px;flex:none}
  .contacts .accent{color:var(--blue)}
  .card-back .brand{
    position:absolute;right:34px;top:40px;gap:8px;
  }
  .card-back .brand-dot{width:14px;height:14px;background:var(--blue)}
  .card-back .brand-name{font-size:17px;letter-spacing:1.5px;color:var(--blue)}
  .address{
    position:absolute;right:38px;top:200px;
    text-align:right;
    font-size:12px;
    line-height:17px;
    color:var(--ink);
  }
</style>
</head>
<body>

<section class="card card-front" aria-label="Card front">
  <div class="brand">
    <span class="brand-dot"></span>
    <span class="brand-name">Valto Sàrl</span>
  </div>
</section>

<section class="card card-back" aria-label="Card back">
  <svg class="wave" viewBox="0 0 520 297" aria-hidden="true">
    <path d="M0 178 C110 232 260 238 400 252 C455 258 495 272 520 297 L0 297 Z" fill="var(--blue-mid)"/>
    <path d="M0 168 C110 222 260 228 400 242 C455 248 495 264 520 292" fill="none" stroke="var(--black)" stroke-width="2.5"/>
    <path d="M0 174 C110 228 260 234 400 248 C455 254 495 268 520 295" fill="none" stroke="var(--paper)" stroke-width="3"/>
  </svg>

  <div class="identity">
    <p class="person-name">Lionel Favre</p>
    <p class="person-role">President</p>
  </div>
  <div class="rule"></div>

  <ul class="contacts">
    <li>
      <svg viewBox="0 0 10 10"><path d="M2 1 L4 1 L4.6 3.2 L3.4 4 Q4.3 5.8 6 6.6 L6.8 5.4 L9 6 L9 8 Q8.6 9 7.5 9 Q1 8.2 1 2.5 Q1 1.4 2 1Z" fill="var(--blue)"/></svg>
      021-555-0148
    </li>
    <li>
      <svg viewBox="0 0 10 10"><rect x="0.7" y="2" width="8.6" height="6" fill="none" stroke="var(--blue)"/><path d="M0.7 2 L5 5.5 L9.3 2" fill="none" stroke="var(--blue)"/></svg>
      info@valto-sarl.ch
    </li>
    <li>
      <svg viewBox="0 0 10 10"><circle cx="5" cy="5" r="4.2" fill="none" stroke="var(--blue)"/><ellipse cx="5" cy="5" rx="1.8" ry="4.2" fill="none" stroke="var(--blue)"/><path d="M0.8 5 H9.2" stroke="var(--blue)"/></svg>
      <span>www.<span class="accent">valto-sarl</span>.ch</span>
    </li>
  </ul>

  <div class="brand">
    <span class="brand-dot"></span>
    <span class="brand-name">Valto Sàrl</span>
  </div>

  <address class="address" style="font-style:normal">
    Chemin des Prés 9<br>
    1027 Lonay
  </address>
</section>

</body>
</html>
```